New site for parent-to-parent advice in spanish requieres Wordpress design

Cunabrisa.com ("time for child" in spanish) is a web site dedicated to give support from father to father in order to attend small babies and childs. The core idea is that divorced, single or widow male parents can get advice from other parents on attending our kids alone, as for short term visits or as single parents. It must be fun and easy to navigate, simple, practical and male-oriented. The site will be in spanish and Mexico and Latin-america market. Some subcategories will be ages of kids (toddlers, kids, preadolescents, adolescents; Bebés, Niños, Preadolescentes, Adolescentes) and other will be the father situation (widows, singles, divorced or even married; Viudos, Solteros, Divorciados, Casados).
Updates

Project Deadline Extended
Reason: As some of your questions are if it includes Wordpress Code and the answer is yes, we are recibed request to extend the deadline to workdays in order to can get the code over an unpdated designs. Thanks.

Target Market(s)

Divorced, single or widow male parents can get advice from other parents on attending our kids alone, as for short term visits or as single parents. The site will be in spanish an Latin-America oriented.

Industry/Entity Type

It Support

Requirements
Must have
• Cunabrisa.com as the name of the site.
Space for banners well identified, in order to sell publicity but to clearly states wich is advice from the team and what paid publicity.
Nice to have
• Penguins will be prefered as the site mascot or graphic elements, since Penguins are the only animal in which male parent keep in charge of the small ones alone for six months a year -view photo for reference, not necesarly for direct use-
Pajarored and Amigored buttons.

```html
<!DOCTYPE html>
<html lang="es">
<head>
<meta charset="utf-8">
<title>Cunabrisa.com</title>
<link rel="stylesheet" href="https://fonts.googleapis.com/css2?family=Bebas+Neue&family=Arimo:wght@400;700&family=Lobster+Two:wght@700&display=swap">
<style>
:root{
  --sky:#8ccbe6;
  --sky-deep:#4a9fcb;
  --hero-top:#6fb6da;
  --hero-bottom:#2f7fae;
  --nav:#2c6f92;
  --nav-dark:#1f2f3b;
  --slate:#24323d;
  --slate-tab:#4b5d70;
  --cream:#fbf3df;
  --steel:#5f87a6;
  --card-blue:#5a9cc4;
  --side:#4fa3cf;
  --side-head:#2f7eab;
  --text:#2a2a2a;
  --white:#ffffff;
  --link:#3c7fb0;
  --social-a:#2f5fa8;
  --social-b:#2fa7df;
}
*{box-sizing:border-box;margin:0;padding:0}
html,body{width:791px;height:1200px;overflow:hidden}
body{position:relative;background:var(--cream);font-family:"Arimo",Arial,sans-serif;color:var(--text)}
.abs{position:absolute}
.display{font-family:"Bebas Neue",Impact,sans-serif;letter-spacing:.3px;font-weight:400}

/* header */
.site-header{left:0;top:0;width:791px;height:83px;background:linear-gradient(#a9dcf1,var(--sky))}
.brand{left:164px;top:24px;display:flex;align-items:center;gap:8px;white-space:nowrap}
.brand-mark{width:24px;height:24px;border-radius:50%;background:var(--slate);flex:none}
.brand-name{font-family:"Bebas Neue",Impact,sans-serif;font-size:27px;color:var(--slate);line-height:1}
.tagline{left:340px;top:25px;width:250px;font-size:16px;line-height:17px;color:var(--white)}
.social{display:flex;gap:6px}
.social a{width:32px;height:34px;display:flex;align-items:flex-end;justify-content:center;padding-bottom:3px;font-family:"Bebas Neue",Impact,sans-serif;font-size:8px;color:var(--white);text-decoration:none}
.social .amigored{background:var(--social-a)}
.social .pajarored{background:var(--social-b)}
.header-social{left:560px;top:24px}

/* nav */
.main-nav{left:0;top:83px;width:791px;height:22px;background:var(--nav)}
.nav-inner{left:151px;top:0;width:481px;height:22px;background:var(--nav-dark);display:flex;align-items:center;justify-content:space-between;padding:0 4px}
.nav-inner span{font-family:"Bebas Neue",Impact,sans-serif;font-size:11.5px;color:var(--white);padding:4px 5px;white-space:nowrap;line-height:1}
.nav-inner .active{background:#3f4f5d}
.nav-inner i{width:3px;height:3px;background:var(--white);border-radius:50%;flex:none}
.dropdown{left:346px;top:105px;width:82px;height:62px;background:var(--nav-dark);padding:3px 0;z-index:3}
.dropdown li{list-style:none;font-size:8.5px;font-weight:700;color:var(--white);padding:2px 10px;height:14px}
.dropdown li.current{background:var(--sky-deep)}

/* hero */
.hero{left:0;top:105px;width:791px;height:226px;background:linear-gradient(var(--hero-top),var(--hero-bottom))}
.hero-photo{left:280px;top:0;width:347px;height:226px;background:linear-gradient(90deg,rgba(111,179,216,0),#d9b59a 35%,#c89c83 70%,#6aa9cf)}
.hero-title{left:164px;top:17px;font-size:34px;color:var(--white);line-height:1;white-space:nowrap;z-index:2}
.hero-text{left:164px;top:88px;width:160px;font-size:14.5px;line-height:15.5px;color:var(--white);z-index:2}
.hero-arrow{top:88px}
.hero-arrow.prev{left:96px}
.hero-arrow.next{left:670px}

/* slide tabs */
.slide-tabs{left:0;top:331px;width:791px;height:43px;background:var(--slate)}
.tab{top:6px;width:110px;text-align:center;color:var(--white)}
.tab h3{font-family:"Bebas Neue",Impact,sans-serif;font-weight:400;font-size:16px;color:#8fd0ee}
.tab p{font-size:6px;line-height:7px;margin-top:2px}
.tab.active{top:-7px;height:56px;background:var(--slate-tab);padding-top:13px}

/* tips */
.tips-box{left:163px;top:383px;width:464px;height:57px;background:var(--steel);border-left:3px solid #42596d}
.tips-box h2{position:absolute;left:5px;top:2px;font-size:22px;color:var(--white);font-weight:400}
.tips-box p{position:absolute;left:6px;top:26px;width:450px;font-size:7.5px;font-style:italic;line-height:9px;color:var(--white);text-align:center}
.tips-ctrl{position:absolute;left:436px;top:3px;width:24px;height:12px;background:#e6e6e6;display:flex;justify-content:space-around;align-items:center;font-size:8px;color:#333}

/* ad banners */
.ad-social{left:163px;width:307px;height:43px;background:var(--white);border:1px solid #c8cfdc}
.ad-social .bar{height:16px;background:var(--social-a);color:var(--white);font-weight:700;font-size:11px;padding:1px 5px}
.ad-social .body{display:flex;align-items:center;padding:6px 5px;font-size:10px;font-weight:700;color:#222;gap:8px;white-space:nowrap}
.ad-social .body em{font-style:normal;font-weight:400;color:var(--social-a);font-size:9px}
.ad-social .cta{margin-left:auto;background:#5a9c3a;color:var(--white);font-size:7px;padding:3px 5px}

/* articles */
.article{left:163px;width:307px;height:74px}
.article .icon{position:absolute;left:0;top:0;width:72px;height:72px;background:var(--card-blue)}
.article h4{position:absolute;left:78px;top:0;font-family:"Bebas Neue",Impact,sans-serif;font-weight:400;font-size:13px;color:#222}
.article p{position:absolute;left:78px;top:16px;width:228px;font-size:8.4px;line-height:11px;color:#333}
.article .more{position:absolute;right:0;bottom:-4px;font-size:8px;font-style:italic;color:var(--link);text-decoration:underline}

/* sidebar */
.sidebar{left:480px;top:453px;width:147px;height:401px;background:var(--side)}
.side-head{background:var(--side-head);color:var(--white);font-family:"Lobster Two",cursive;font-size:17px;padding:2px 7px;height:27px;white-space:nowrap}
.side-list{padding:4px 0 6px 22px;color:var(--white);font-size:9.5px;line-height:14.5px}
.ad-rent{left:480px;top:860px;width:147px;height:125px;background:var(--white);border:1px solid #ccc;text-align:center}
.ad-rent .title{font-size:14px;color:#1b5fa8;padding-top:5px;line-height:15px}
.ad-rent .sub{font-size:5.5px;color:#c33;font-weight:700}
.ad-rent .deal{font-size:9.5px;color:#1b5fa8;margin-top:6px;line-height:11px}
.ad-rent .photo{position:absolute;left:6px;top:78px;width:134px;height:42px;background:linear-gradient(90deg,#d8b78e,#f1e3c8,#9fb8c8)}
.ad-rent .btn{position:absolute;left:80px;top:88px;background:#e96d1d;color:var(--white);font-size:6px;padding:2px 5px}

/* footer */
.footer-nav{left:0;top:1007px;width:791px;height:23px;background:var(--nav);display:flex;justify-content:center;align-items:center;gap:11px}
.footer-nav span{font-family:"Bebas Neue",Impact,sans-serif;font-size:12.5px;color:var(--white);white-space:nowrap}
.footer-nav i{width:3px;height:3px;background:var(--white);border-radius:50%}
.site-footer{left:0;top:1030px;width:791px;height:170px;background:var(--slate);color:var(--white)}
.fcol{top:12px}
.fcol h5{font-family:"Bebas Neue",Impact,sans-serif;font-weight:400;font-size:10px;margin-bottom:4px}
.fcol ul{padding-left:18px;font-size:6.5px;line-height:8.5px;margin-bottom:10px}
.footer-social{left:400px;top:48px}
.footer-brand{left:498px;top:50px}
.footer-brand .brand-name{color:#8fd0ee;font-size:34px}
.footer-brand .brand-mark{background:#8fd0ee}
.legal{left:0;top:151px;width:791px;text-align:center;font-size:6px;line-height:9px;color:var(--white)}
.legal span{margin:0 5px}
</style>
</head>
<body>

<header class="site-header abs">
  <div class="brand abs"><span class="brand-mark"></span><span class="brand-name">Cunabrisa.com</span></div>
  <p class="tagline abs display">Lorem ipsum dolor sit amet,<br>consectetur adipiscing elit. Phasellus</p>
  <div class="social header-social abs"><a class="amigored">Amigored</a><a class="pajarored">Pajarored</a></div>
</header>

<nav class="main-nav abs">
  <div class="nav-inner abs">
    <span class="active">Inicio</span><i></i><span>Primeros Pasos</span><i></i><span>Padre a Padre</span><i></i><span>Hijos por Edades</span><i></i><span>Situacion del Padre</span><i></i><span>Nosotros</span><i></i><span>Contactos</span>
  </div>
</nav>
<ul class="dropdown abs">
  <li>Bebés</li><li class="current">Niños</li><li>Preadolescentes</li><li>Adolescentes</li>
</ul>

<section class="hero abs">
  <div class="hero-photo abs" role="img" aria-label="Fotografía de un padre y su hijo pequeño frente a frente, juntando sus frentes"></div>
  <h1 class="hero-title abs display">¿Lorem ipsum?</h1>
  <p class="hero-text abs display">Lorem ipsum dolor sit amet, consectetur adipiscing elit. Phasellus dictum scelerisque ipsum ac sodales.</p>
  <svg class="hero-arrow prev abs" width="22" height="50" viewBox="0 0 22 50"><path d="M18 2 L4 25 L18 48" fill="none" stroke="#1f3a4d" stroke-width="5"/></svg>
  <svg class="hero-arrow next abs" width="22" height="50" viewBox="0 0 22 50"><path d="M4 2 L18 25 L4 48" fill="none" stroke="#1f3a4d" stroke-width="5"/></svg>
</section>

<section class="slide-tabs abs">
  <div class="tab active abs" style="left:163px"><h3>¿Lorem ipsum?</h3><p>Lorem ipsum dolor sit amet, consectetur adipiscing elit.</p></div>
  <div class="tab abs" style="left:290px"><h3>¿Lorem ipsum?</h3><p>Lorem ipsum dolor sit amet, consectetur adipiscing elit.</p></div>
  <div class="tab abs" style="left:405px"><h3>¿Lorem ipsum?</h3><p>Lorem ipsum dolor sit amet, consectetur adipiscing elit.</p></div>
  <div class="tab abs" style="left:520px"><h3>¿Lorem ipsum?</h3><p>Lorem ipsum dolor sit amet, consectetur adipiscing elit.</p></div>
</section>

<section class="tips-box abs">
  <h2 class="display">Tips!</h2>
  <div class="tips-ctrl"><span>‹</span><span>›</span></div>
  <p>Lorem ipsum dolor sit amet, consectetur adipiscing elit. Vivamus nec sodales ligula. Aenean tincidunt vitae ante eget faucibus. Vivamus ac diam diam. Sed ac sapien cursus diam sagittis consequat sit amet sit amet lectus.</p>
</section>

<aside class="ad-social abs" style="top:453px">
  <div class="bar">Amigored</div>
  <div class="body">Create an Amigored profile <em>Sign up for free today!</em><span class="cta">Sign Up</span></div>
</aside>

<article class="article abs" style="top:510px">
  <div class="icon" role="img" aria-label="Icono de huella de pie"></div>
  <h4>Primeros Pasos</h4>
  <p>Lorem ipsum dolor sit amet, consectetur adipiscing elit. Vivamus nec sodales ligula. Aenean tincidunt vitae ante eget faucibus. Vivamus ac diam diam. Sed ac sapien cursus diam sagittis consequat sit amet sit amet lectus.</p>
  <span class="more">Ver más...</span>
</article>
<article class="article abs" style="top:590px">
  <div class="icon" role="img" aria-label="Icono de dos personas"></div>
  <h4>Padre a Padre</h4>
  <p>Lorem ipsum dolor sit amet, consectetur adipiscing elit. Vivamus nec sodales ligula. Aenean tincidunt vitae ante eget faucibus. Vivamus ac diam diam. Sed ac sapien cursus diam sagittis consequat sit amet sit amet lectus.</p>
  <span class="more">Ver más...</span>
</article>

<aside class="ad-social abs" style="top:671px">
  <div class="bar">Amigored</div>
  <div class="body">Create an Amigored profile <em>Sign up for free today!</em><span class="cta">Sign Up</span></div>
</aside>

<article class="article abs" style="top:723px">
  <div class="icon" role="img" aria-label="Icono de silueta de persona"></div>
  <h4>Hijos por Edades</h4>
  <p>Lorem ipsum dolor sit amet, consectetur adipiscing elit. Vivamus nec sodales ligula. Aenean tincidunt vitae ante eget faucibus. Vivamus ac diam diam. Sed ac sapien cursus diam sagittis consequat sit amet sit amet lectus.</p>
  <span class="more">Ver más...</span>
</article>
<article class="article abs" style="top:803px">
  <div class="icon" role="img" aria-label="Icono de grupo de personas"></div>
  <h4>Situacion del Padre</h4>
  <p>Lorem ipsum dolor sit amet, consectetur adipiscing elit. Vivamus nec sodales ligula. Aenean tincidunt vitae ante eget faucibus. Vivamus ac diam diam. Sed ac sapien cursus diam sagittis consequat sit amet sit amet lectus.</p>
  <span class="more">Ver más...</span>
</article>
<article class="article abs" style="top:882px">
  <div class="icon" role="img" aria-label="Icono de sol"></div>
  <h4>Tips</h4>
  <p>Lorem ipsum dolor sit amet, consectetur adipiscing elit. Vivamus nec sodales ligula. Aenean tincidunt vitae ante eget faucibus. Vivamus ac diam diam. Sed ac sapien cursus diam sagittis consequat sit amet sit amet lectus.</p>
  <span class="more">Ver más...</span>
</article>

<nav class="sidebar abs">
  <h3 class="side-head">Primeros Pasos</h3>
  <ul class="side-list"><li>Lorem Ipsum</li><li>Dolor sit amet</li><li>Consectetur</li><li>Adipiscing elit</li></ul>
  <h3 class="side-head">Padre a Padre</h3>
  <ul class="side-list"><li>Lorem Ipsum</li><li>Dolor sit amet</li><li>Consectetur</li><li>Adipiscing elit</li></ul>
  <h3 class="side-head">Hijos por Edades</h3>
  <ul class="side-list"><li>Bebés</li><li>Niños</li><li>Preadolescentes</li><li>Adolescentes</li></ul>
  <h3 class="side-head">Situacion del Padre</h3>
  <ul class="side-list"><li>Viudos</li><li>Solteros</li><li>Divorciados</li><li>Casados</li></ul>
  <h3 class="side-head">Tips</h3>
</nav>

<aside class="ad-rent abs">
  <p class="title">Apartamentos Temporales</p>
  <p class="sub">EL MEJOR PRECIO EN LOS MEJORES APARTAMENTOS</p>
  <p class="deal">LAS MEJORES OFERTAS EN TEMPORADA ALTA</p>
  <div class="photo" role="img" aria-label="Fotografía del interior de un apartamento"></div>
  <span class="btn">INFÓRMESE YA</span>
</aside>

<nav class="footer-nav abs">
  <span>Inicio</span><i></i><span>Primeros Pasos</span><i></i><span>Padre a Padre</span><i></i><span>Hijos por Edades</span><i></i><span>Situacion del Padre</span><i></i><span>Nosotros</span><i></i><span>Contactos</span>
</nav>

<footer class="site-footer abs">
  <div class="fcol abs" style="left:163px">
    <h5>Inicio</h5>
    <h5>Primeros Pasos</h5>
    <ul><li>Lorem Ipsum</li><li>Dolor sit amet</li><li>Consectetur</li><li>Adipiscing elit</li></ul>
    <h5>Padre a Padre</h5>
    <ul><li>Lorem Ipsum</li><li>Dolor sit amet</li><li>Consectetur</li><li>Adipiscing elit</li></ul>
  </div>
  <div class="fcol abs" style="left:281px">
    <h5>Hijos por Edades</h5>
    <ul><li>Bebés</li><li>Niños</li><li>Preadolescentes</li><li>Adolescentes</li></ul>
    <h5>Situacion del Padre</h5>
    <ul><li>Viudos</li><li>Solteros</li><li>Divorciados</li><li>Casados</li></ul>
  </div>
  <div class="fcol abs" style="left:400px">
    <h5>Nosotros</h5>
    <h5>Contactos</h5>
  </div>
  <div class="social footer-social abs"><a class="amigored">Amigored</a><a class="pajarored">Pajarored</a></div>
  <div class="brand footer-brand abs"><span class="brand-mark"></span><span class="brand-name">Cunabrisa.com</span></div>
  <div class="legal abs">
    <p><span>Terms and Conditions</span><span>Privacy Policy</span><span>How It Works</span><span>Acceptable Use Policy</span></p>
    <p>© 2013 Cunabrisa.com. All rights reserved.</p>
  </div>
</footer>

</body>
</html>
```